Retail Supplement Store Flyer for Fitness Centers

We need a flyer that highlights our top selling products to gain more customers from local fitness center members. We are a retailer that carries the highest lab tested quality of a large variety of fitness supplements including protein, creatine, vitamins pre-workout powder, Sarms and Peptides and much more. We would need to add our store phone number, address and business information to the flyer.

```html
<!DOCTYPE html>
<html lang="en">
<head>
<meta charset="utf-8">
<title>Peak Form Supplements – Flyer</title>
<link href="https://fonts.googleapis.com/css2?family=Anton&family=Oswald:wght@500;600&family=Open+Sans:wght@400;600;700&display=swap" rel="stylesheet">
<style>
  :root{
    --red:#e8191b;
    --navy:#0d2b5c;
    --navy-text:#1d3a6e;
    --grey:#86888c;
    --white:#ffffff;
    --wood:#d59a5c;
    --wood-dark:#b97b3f;
  }
  *{margin:0;padding:0;box-sizing:border-box}
  html,body{width:927px;height:1200px;overflow:hidden;background:var(--white)}
  .flyer{position:relative;width:927px;height:1200px;overflow:hidden;font-family:"Open Sans",Arial,sans-serif}
  .gym-backdrop{position:absolute;left:0;top:0;width:927px;height:720px;
    background:radial-gradient(ellipse at 50% 40%,#fbfbfb 0%,#eeeeee 45%,#d9d7d4 100%)}
  .shelf{position:absolute;left:0;top:719px;width:927px;height:152px;
    background:linear-gradient(180deg,#e2ae73 0%,var(--wood) 45%,var(--wood-dark) 100%)}
  .plate{position:absolute;background:var(--navy)}
  .headline{position:absolute;left:0;top:0}
  .intro{position:absolute;left:180px;top:304px;width:580px;text-align:center;
    color:var(--navy-text);font-size:17px;line-height:24.5px}
  .products-banner{position:absolute;left:194px;top:426px;width:539px;height:43px;background:var(--red);
    color:var(--white);font-family:"Oswald",sans-serif;font-weight:600;font-size:29px;line-height:43px;
    text-align:center;letter-spacing:.2px}
  .product{position:absolute}
  .product.bottle{border-radius:26px 26px 18px 18px;background:linear-gradient(90deg,#111 0%,#333 45%,#0c0c0c 100%)}
  .product.vial{border-radius:18px 18px 14px 14px;background:linear-gradient(90deg,#c9ced6 0%,#f4f6f9 40%,#aeb6c3 100%)}
  .info-band{position:absolute;left:0;top:871px;width:927px;height:329px;background:var(--navy)}
  .why-title{position:absolute;left:55px;top:899px;width:401px;height:44px;background:var(--red);
    color:var(--white);font-family:"Oswald",sans-serif;font-weight:600;font-size:25px;line-height:44px;text-align:center}
  .why-list{position:absolute;left:55px;top:956px;list-style:none;color:var(--white);font-size:19.5px;line-height:22px}
  .why-list li{position:relative;padding-left:26px;margin-bottom:13px}
  .why-list li::before{content:"";position:absolute;left:0;top:7px;width:15px;height:12px;background:var(--red);
    clip-path:polygon(0 0,100% 0,100% 60%,50% 100%,0 60%)}
  .cta-panel{position:absolute;left:490px;top:897px;width:382px;height:303px;background:var(--grey)}
  .cta-title{position:absolute;left:26px;top:12px;color:var(--navy);font-family:"Oswald",sans-serif;font-weight:600;
    font-size:26px;line-height:28px;letter-spacing:.2px}
  .cta-text{position:absolute;left:26px;top:90px;width:340px;color:var(--white);font-size:16px;line-height:23px}
  .footer{position:absolute;left:0;top:1090px;width:927px;height:86px;background:var(--red)}
  .brand{position:absolute;left:59px;top:16px;display:flex;align-items:center;gap:10px;color:var(--white);
    font-family:"Oswald",sans-serif;font-weight:600}
  .brand-dot{width:44px;height:44px;border-radius:50%;background:var(--white)}
  .brand-name{font-size:30px;line-height:30px;letter-spacing:1px}
  .brand-sub{display:block;font-size:13px;line-height:18px;letter-spacing:7.4px}
  .footer-divider{position:absolute;left:383px;top:15px;width:3px;height:57px;background:var(--white)}
  .contact{position:absolute;left:406px;top:16px;color:var(--white)}
  .contact-address{font-weight:700;font-size:18.5px;line-height:26px}
  .contact-line{font-size:17px;line-height:30px}
  .contact-line .sep{margin:0 8px}
  .contact-line strong{font-weight:700}
</style>
</head>
<body>
<main class="flyer">
  <div class="gym-backdrop" role="img" aria-label="Softly blurred bright gym interior background"></div>
  <div class="shelf" role="img" aria-label="Light wooden shelf surface"></div>

  <div class="plate" style="left:78px;top:95px;width:36px;height:115px"></div>
  <div class="plate" style="left:129px;top:62px;width:36px;height:180px"></div>
  <div class="plate" style="left:182px;top:25px;width:34px;height:255px"></div>
  <div class="plate" style="left:711px;top:25px;width:35px;height:255px"></div>
  <div class="plate" style="left:762px;top:62px;width:35px;height:180px"></div>
  <div class="plate" style="left:813px;top:95px;width:35px;height:115px"></div>

  <svg class="headline" width="927" height="270" viewBox="0 0 927 270">
    <text x="231" y="125" fill="#e8191b" font-family="Anton, sans-serif" font-size="112" textLength="462" lengthAdjust="spacingAndGlyphs">FUEL YOUR</text>
    <rect x="231" y="142" width="464" height="18" fill="#0d2b5c"/>
    <text x="231" y="227" fill="#e8191b" font-family="Anton, sans-serif" font-size="68" textLength="462" lengthAdjust="spacingAndGlyphs">FITNESS GOALS</text>
    <text x="233" y="257" fill="#e8191b" font-family="Oswald, sans-serif" font-weight="600" font-size="22" textLength="460" lengthAdjust="spacing">WITH PREMIUM SUPPLEMENTS!</text>
  </svg>

  <p class="intro">At Peak Form Supplements, we provide the highest lab-tested quality fitness supplements to help you crush your goals. Whether you’re building strength, boosting energy, or improving recovery, we’ve got you covered.</p>

  <div class="products-banner">OUR TOP-SELLING PRODUCTS INCLUDE</div>

  <div class="product bottle" style="left:79px;top:496px;width:152px;height:288px" role="img" aria-label="Black supplement bottle with pink label"></div>
  <div class="product bottle" style="left:286px;top:496px;width:152px;height:288px" role="img" aria-label="Black supplement bottle with yellow label"></div>
  <div class="product vial" style="left:506px;top:496px;width:128px;height:284px" role="img" aria-label="Glass product vial with blue and white label"></div>
  <div class="product vial" style="left:712px;top:496px;width:128px;height:284px" role="img" aria-label="Glass product vial with blue and white label"></div>

  <section class="info-band">
  </section>

  <h2 class="why-title">WHY CHOOSE US?</h2>
  <ul class="why-list">
    <li>Trusted by fitness enthusiasts.</li>
    <li>Wide variety to suit your needs.</li>
    <li>Expert guidance to find the right<br>products for you.</li>
  </ul>

  <section class="cta-panel">
    <h2 class="cta-title">READY TO TAKE YOUR FITNESS<br>TO THE NEXT LEVEL?</h2>
    <p class="cta-text">Visit us today and see why local fitness center members trust us for all their supplement needs.</p>
  </section>

  <footer class="footer">
    <div class="brand">
      <span class="brand-dot"></span>
      <span class="brand-name">PEAK FORM<span class="brand-sub">SUPPLEMENTS</span></span>
    </div>
    <div class="footer-divider"></div>
    <div class="contact">
      <p class="contact-address">480 Ridgeway Avenue, Lakeview, IL 60613, USA</p>
      <p class="contact-line">hello@peakformstore.com<span class="sep">|</span><strong>+1 (555) 302-4817</strong></p>
    </div>
  </footer>
</main>
</body>
</html>
```